R & T Summit Construction Business Card ideas

We want a business card to represents our company in a way that looks professional but is also a business card that is unique!

Industry/Entity Type

Construction Company

Contact Information for Business Card

open to all design ideas, just want to be able to see different options to choose from in either color or grayscale.

Requirements
Must have
• Our names and phone numbers
• Nolan Pritchett 512-804-2271
• Curtis Hale 512-693-1804
• Business logo

```html
<!DOCTYPE html>
<html lang="en">
<head>
<meta charset="utf-8">
<title>R &amp; T Summit Construction – Business Card</title>
<link rel="stylesheet" href="https://fonts.googleapis.com/css2?family=Cinzel:wght@400;700&family=Source+Sans+3:wght@400&display=swap">
<style>
  :root {
    --backdrop: #e9e6e2;
    --paper: #ffffff;
    --ink: #1a1a1a;
    --ink-soft: #3c3c3c;
    --muted: #6a6a6a;
    --rule: #bdbdbd;
    --night: #060606;
    --on-night: #ffffff;
  }
  * { margin: 0; padding: 0; box-sizing: border-box; }
  html, body {
    width: 1200px; height: 987px; overflow: hidden;
    background: var(--backdrop);
  }
  .stage { position: relative; width: 1200px; height: 987px; }
  .card {
    position: absolute; left: 293px; width: 615px; height: 351px;
  }
  .card--front { top: 130px; background: var(--paper); }
  .card--back { top: 506px; background: var(--night); }

  .brand {
    position: absolute; display: flex; align-items: center; gap: 10px;
    font-family: "Cinzel", serif; font-weight: 700; line-height: 1.05;
  }
  .brand__mark { flex: none; width: 14px; height: 14px; }
  .card--front .brand { left: 36px; top: 142px; width: 240px; font-size: 22px; color: var(--ink); }
  .card--front .brand__mark { background: var(--ink); }
  .card--back .brand { left: 142px; top: 115px; width: 340px; font-size: 31px; color: var(--on-night); }
  .card--back .brand__mark { width: 18px; height: 18px; background: var(--on-night); }

  .divider {
    position: absolute; left: 301px; top: 84px; width: 1px; height: 184px;
    background: var(--rule);
  }
  .contact { position: absolute; left: 325px; top: 84px; font-family: "Source Sans 3", sans-serif; }
  .contact__name {
    font-family: "Cinzel", serif; font-weight: 700; font-size: 24px;
    color: var(--ink); letter-spacing: 0.5px; line-height: 1.1;
  }
  .contact__title {
    font-family: "Cinzel", serif; font-weight: 400; font-size: 18px;
    color: var(--muted); line-height: 1.1; margin-bottom: 16px;
  }
  .contact__address { font-size: 16.5px; color: var(--ink-soft); line-height: 23px; margin-bottom: 10px; }
  .contact__line {
    display: flex; align-items: center; gap: 9px;
    font-size: 16.5px; color: var(--ink-soft); line-height: 23.5px;
  }
  .contact__line svg { width: 13px; height: 14px; flex: none; fill: var(--ink); }

  .web {
    position: absolute; left: 0; right: 0; top: 287px; text-align: center;
    font-family: "Cinzel", serif; font-size: 17px; letter-spacing: 5px;
    color: var(--on-night);
  }
</style>
</head>
<body>
<main class="stage">
  <section class="card card--front">
    <div class="brand"><span class="brand__mark"></span><span>R &amp; T Summit Construction</span></div>
    <div class="divider"></div>
    <div class="contact">
      <p class="contact__name">NOLAN PRITCHETT</p>
      <p class="contact__title">CEO/Founder</p>
      <p class="contact__address">2140 Cedar Ridge Drive<br>Austin, Texas 78704</p>
      <p class="contact__line">
        <svg viewBox="0 0 12 16" aria-hidden="true"><path d="M2 0h8a2 2 0 0 1 2 2v12a2 2 0 0 1-2 2H2a2 2 0 0 1-2-2V2a2 2 0 0 1 2-2zm0 2v10h8V2zm4 11a1 1 0 1 0 0 2 1 1 0 0 0 0-2z"/></svg>
        512-804-2271
      </p>
      <p class="contact__line">
        <svg viewBox="0 0 14 12" aria-hidden="true"><path d="M0 2h14v1L7 7 0 3zM0 4.2l7 4 7-4V11H0z"/></svg>
        npritchett@rtsummitbuild.com
      </p>
      <p class="contact__line">
        <svg viewBox="0 0 14 14" aria-hidden="true"><circle cx="7" cy="7" r="7"/><path d="M4 4l3 1 1 3-2 1-1 3-1-3-2-1z" fill="#fff"/></svg>
        www.rtsummitbuild.com
      </p>
    </div>
  </section>

  <section class="card card--back">
    <div class="brand"><span class="brand__mark"></span><span>R &amp; T Summit Construction</span></div>
    <p class="web">www.rtsummitbuild.com</p>
  </section>
</main>
</body>
</html>
```